Larkspur Ridge Management - Business Cards

I need business cards. My current logo was designed by a designer at this site and I very much like and am happy with the results. I would like a business card that is trendy, unique, current yet professional. I deal with high net worth clients daily

Target Market(s)

Out of state investors looking to get into the rental market in Ohio

Industry/Entity Type

Property Management, Consulting

Contact Information for Business Card

Name, Title (Chief Financial Officer) office phone number (555) 817-3094 website address larkridgemgmt.example

Font styles to use
Sans Serif

Colors
0054AA
0677BA
7BADD7
CADEEF
E8F1F8
0094D4
00A9DD
6FCCEA
C7EBF8
E9F6FB
00AB8E
00BBA5
67D7C9
C6EFE9
E9F9F6

```html
<!DOCTYPE html>
<html lang="en">
<head>
<meta charset="UTF-8">
<title>Larkspur Ridge Management – Business Cards</title>
<link rel="stylesheet" href="https://fonts.googleapis.com/css2?family=Poppins:wght@400;600;700&display=swap">
<style>
  :root {
    --navy: #22345a;
    --red: #d0202b;
    --white: #ffffff;
    --ink: #22345a;
    --stage: #e9edf2;
  }
  * { margin: 0; padding: 0; box-sizing: border-box; }
  html, body { width: 1200px; height: 875px; overflow: hidden; }
  body {
    background: var(--stage);
    font-family: "Poppins", sans-serif;
    position: relative;
  }
  .card {
    position: absolute;
    width: 540px;
    height: 310px;
    border-radius: 18px;
    overflow: hidden;
    box-shadow: 0 10px 28px rgba(20, 30, 50, 0.18);
  }
  .card-front {
    left: 60px;
    top: 110px;
    background: var(--navy);
    display: flex;
    align-items: center;
    justify-content: center;
  }
  .front-brand {
    display: flex;
    align-items: center;
    gap: 14px;
    color: var(--white);
    font-weight: 700;
    font-size: 26px;
    line-height: 1.15;
    text-transform: uppercase;
    letter-spacing: 0.5px;
  }
  .front-brand .mark {
    width: 22px;
    height: 22px;
    border-radius: 50%;
    background: var(--red);
    flex: none;
  }
  .card-back {
    left: 600px;
    top: 455px;
    background: var(--white);
  }
  .back-brand {
    position: absolute;
    right: 34px;
    top: 38px;
    text-align: right;
    color: var(--ink);
    font-weight: 700;
    font-size: 17px;
    line-height: 1.2;
    text-transform: uppercase;
  }
  .brand-rule {
    position: absolute;
    left: 34px;
    right: 34px;
    top: 112px;
    height: 1.5px;
    background: var(--navy);
  }
  .holder {
    position: absolute;
    left: 34px;
    top: 138px;
  }
  .holder-name {
    color: var(--ink);
    font-weight: 700;
    font-size: 21px;
    text-transform: uppercase;
    line-height: 1.1;
  }
  .holder-title {
    color: var(--ink);
    font-size: 12.5px;
    margin-top: 2px;
  }
  .holder-rule {
    width: 190px;
    height: 1.5px;
    background: var(--navy);
    margin: 9px 0 9px;
  }
  .contact-list { list-style: none; }
  .contact-list li {
    display: flex;
    align-items: center;
    gap: 9px;
    font-size: 12.5px;
    color: var(--ink);
    line-height: 1.55;
  }
  .contact-list svg { width: 11px; height: 11px; fill: var(--red); flex: none; }
  .bands {
    position: absolute;
    left: 0;
    bottom: 0;
    width: 540px;
    height: 40px;
  }
</style>
</head>
<body>

  <section class="card card-front">
    <div class="front-brand">
      <span class="mark"></span>
      <span>Larkspur Ridge<br>Management</span>
    </div>
  </section>

  <section class="card card-back">
    <div class="back-brand">Larkspur Ridge<br>Management</div>
    <div class="brand-rule"></div>

    <div class="holder">
      <p class="holder-name">Daniel Hartwell</p>
      <p class="holder-title">Chief Financial Officer</p>
      <div class="holder-rule"></div>
      <ul class="contact-list">
        <li>
          <svg viewBox="0 0 24 24"><path d="M6.6 10.8a15 15 0 0 0 6.6 6.6l2.2-2.2c.3-.3.7-.4 1-.2 1.1.4 2.3.6 3.6.6.6 0 1 .4 1 1V20c0 .6-.4 1-1 1A17 17 0 0 1 3 4c0-.6.4-1 1-1h3.5c.6 0 1 .4 1 1 0 1.3.2 2.5.6 3.6.1.3 0 .7-.2 1z"/></svg>
          1 (555) 817-3094
        </li>
        <li>
          <svg viewBox="0 0 24 24"><path d="M2 5h20v14H2z M2 5l10 8 10-8" /></svg>
          info@larkridgemgmt.example
        </li>
        <li>
          <svg viewBox="0 0 24 24"><circle cx="12" cy="12" r="10"/></svg>
          www.larkridgemgmt.example
        </li>
      </ul>
    </div>

    <svg class="bands" viewBox="0 0 540 40" preserveAspectRatio="none">
      <polygon points="0,34 380,16 372,40 0,40" fill="var(--navy)"/>
      <polygon points="390,15 540,8 540,40 382,40" fill="var(--red)"/>
    </svg>
  </section>

</body>
</html>
```